ZERIFA sweets needs chic packaging designs

We need a packaging design for our new homemade sweets line called Zerifas' Sweets located in the UAE. We have a range of sweets that vary from full cakes to separate cuts, we have 3 types of cookies, and we have sweets usually packed in transparent plastic cups. We usually use the plastic transparent packaging off the counter but we want to step it up a notch and get distinguished through our modern unique packaging that also reflects local Emirati touch of homemade cooking.

For an idea of some of the sweets we post on instagram check out @qolti_uae. Our main clients are employees so we want the packaging to be suitable in size and usability for desk top use, easy quick chic servings. looking for this behavior: the box or package should be attractive so that others could come over and say "wow whats that"
Updates

Target Market(s)

Employees male and female

Font styles to use
Other font styles liked:
• as logo

Colors
ec1f27
0355a3
f37122

Requirements
Must have
• Chic design
• Usability
• Easy handling
• Consistent with brand logo
Nice to have
• Light weight

```html
<!DOCTYPE html>
<html lang="en">
<head>
<meta charset="utf-8">
<title>Sweets Box Dieline</title>
<link rel="stylesheet" href="https://fonts.googleapis.com/css2?family=Questrial&family=Arimo:wght@400;700&display=swap">
<style>
  :root {
    --bg: #8e8e8e;
    --orange: #f37122;
    --orange-fold: #d95f17;
    --blue: #0355a3;
    --navy: #1b2f7a;
    --red: #ec1f27;
    --cyan: #1ba0d8;
    --paper: #f2f2f2;
    --white: #ffffff;
  }
  * { margin: 0; padding: 0; box-sizing: border-box; }
  html, body { width: 709px; height: 1200px; overflow: hidden; background: var(--bg); }
  .canvas { position: relative; width: 709px; height: 1200px; }
  .dieline { position: absolute; inset: 0; }
  .edge-dots {
    position: absolute; width: 8px;
    background: radial-gradient(circle, var(--white) 2.2px, transparent 2.6px) 0 0 / 8px 10px repeat-y;
  }
  .edge-text {
    position: absolute; width: 10px; overflow: hidden;
    font-family: "Arimo", sans-serif; font-size: 7px; color: var(--white);
    writing-mode: vertical-rl; white-space: nowrap; letter-spacing: 0.5px;
  }
  .tab-name {
    position: absolute; left: 255px; width: 201px; top: 16px; text-align: center;
    font-family: "Questrial", sans-serif; font-size: 11px; letter-spacing: 2px;
    color: var(--navy); transform: rotate(180deg);
  }
  .brand-main {
    position: absolute; left: 255px; width: 201px; top: 412px; text-align: center;
    font-family: "Questrial", sans-serif; font-size: 36px; letter-spacing: 4px; color: var(--navy);
  }
  .brand-small {
    position: absolute; left: 255px; width: 201px; top: 640px; text-align: center;
    font-family: "Questrial", sans-serif; font-size: 13px; letter-spacing: 2px; color: var(--navy);
  }
  .maker-info {
    position: absolute; left: 255px; width: 201px; top: 768px; text-align: center;
    font-family: "Arimo", sans-serif; font-size: 11px; line-height: 14px; color: var(--blue);
  }
  .maker-info .label { font-size: 10px; }
</style>
</head>
<body>
<div class="canvas">
  <svg class="dieline" width="709" height="1200" viewBox="0 0 709 1200">
    <defs>
      <linearGradient id="paperTone" x1="0" y1="0" x2="1" y2="1">
        <stop offset="0" stop-color="#f4f4f4"/>
        <stop offset="0.5" stop-color="#e6e6e6"/>
        <stop offset="1" stop-color="#f4f4f4"/>
      </linearGradient>
    </defs>
    <polygon points="28,576 4,592 4,924 28,940" fill="var(--orange)"/>
    <polygon points="685,576 705,592 705,924 685,940" fill="var(--orange)"/>
    <rect x="28" y="36" width="227" height="1128" fill="var(--orange)"/>
    <rect x="456" y="36" width="229" height="1128" fill="var(--orange)"/>
    <g stroke="var(--orange-fold)" stroke-width="1" stroke-dasharray="4 3">
      <line x1="28" y1="228" x2="255" y2="228"/><line x1="456" y1="228" x2="685" y2="228"/>
      <line x1="4" y1="576" x2="255" y2="576"/><line x1="456" y1="576" x2="705" y2="576"/>
      <line x1="4" y1="940" x2="255" y2="940"/><line x1="456" y1="940" x2="705" y2="940"/>
      <line x1="28" y1="1056" x2="255" y2="1056"/><line x1="456" y1="1056" x2="685" y2="1056"/>
      <line x1="28" y1="576" x2="28" y2="940"/><line x1="685" y1="576" x2="685" y2="940"/>
    </g>
    <path d="M255,36 L262,14 Q264,10 270,10 L441,10 Q447,10 449,14 L456,36 L456,1192 L255,1192 Z" fill="var(--paper)"/>
    <rect x="266" y="40" width="179" height="1148" fill="url(#paperTone)" role="img" aria-label="Faint floral pattern background"/>
    <rect x="255" y="36" width="5" height="1156" fill="var(--navy)"/>
    <rect x="260" y="36" width="2" height="1156" fill="var(--red)"/>
    <rect x="262" y="36" width="3" height="1156" fill="var(--cyan)"/>
    <rect x="446" y="36" width="3" height="1156" fill="var(--cyan)"/>
    <rect x="449" y="36" width="2" height="1156" fill="var(--red)"/>
    <rect x="451" y="36" width="5" height="1156" fill="var(--navy)"/>
    <circle cx="355" cy="340" r="48" fill="none" stroke="var(--navy)" stroke-width="2"/>
    <circle cx="355" cy="606" r="20" fill="none" stroke="var(--navy)" stroke-width="1.5"/>
    <circle cx="355.5" cy="1176" r="6" fill="var(--navy)"/>
  </svg>

  <div class="edge-dots" style="left:36px; top:48px; height:1104px;"></div>
  <div class="edge-dots" style="left:669px; top:48px; height:1104px;"></div>
  <div class="edge-dots" style="left:242px; top:48px; height:1104px;"></div>
  <div class="edge-dots" style="left:463px; top:48px; height:1104px;"></div>
  <div class="edge-text" style="left:655px; top:60px; height:1080px;">Homemade sweets • Made fresh daily • Homemade sweets • Made fresh daily • Homemade sweets • Made fresh daily • Homemade sweets • Made fresh daily • Homemade sweets • Made fresh daily • Homemade sweets • Made fresh daily •</div>

  <div class="tab-name">ZERIFA</div>
  <div class="brand-main">ZERIFA</div>
  <div class="brand-small">ZERIFA</div>
  <div class="maker-info">
    <div class="label">Manufactured by:</div>
    <div>Baking Company Name</div>
    <div>Address</div>
    <div>Contact Numbers</div>
    <div>website</div>
    <div>facebook</div>
    <div>twitter account</div>
  </div>
</div>
</body>
</html>
```